brixtane motor oil

I would like to inform you that our new motor oil brand brixtane will be divided into three categories:
Brixtane high performance Full Synthetic
0w20 ,5w30 ,0w16,5w20
with massage.
Maximum Protection, Ultimate Performance.brixtane quendor
--------------------------------
brixtane quendor Synthetic Blend
10w40,5w30,5w20
with massage
The perfect combination of durability and efficiency
-------------------------------
brixtane gelvoria transmission fluid
ATF III
with massage
proven to maximize transmission life

```html
<!DOCTYPE html>
<html lang="en">
<head>
<meta charset="utf-8">
<title>Brixtane Motor Oil – Label Range</title>
<link href="https://fonts.googleapis.com/css2?family=Poppins:wght@300;400;600;700;800&family=Roboto+Condensed:wght@500&display=swap" rel="stylesheet">
<style>
  :root{
    --page:#ffffff;
    --ink:#111a2a;
    --sheet-line:#cfcfcf;
    --dim-line:#1a1a1a;
    --ext-line:#bdbdbd;
    --sky-light:#8ff6ff;
    --sky-mid:#45cdf3;
    --sky-deep:#1f9fe2;
    --stripe:#4aaedc;
    --navy:#081848;
    --navy-mid:#163a8a;
    --gold:#c9a645;
    --gold-light:#efd98a;
    --band:#8ef2fb;
    --dot:#1b8be0;
  }
  html,body{margin:0;padding:0;}
  body{
    width:1200px;height:927px;overflow:hidden;position:relative;
    background:var(--page);
    font-family:"Poppins",sans-serif;color:var(--ink);
  }
  .sheet{position:absolute;inset:0;width:1200px;height:927px;}
  .dim-value{
    position:absolute;transform:translate(-50%,-50%);
    font-family:"Roboto Condensed",sans-serif;font-weight:500;font-size:15px;
    line-height:1;background:var(--page);padding:1px 3px;color:var(--dim-line);
  }

  .label{position:absolute;overflow:hidden;}
  .label svg{position:absolute;inset:0;width:100%;height:100%;display:block;}
  .label--full{left:135px;top:325px;width:190px;height:273px;clip-path:polygon(0 41px,100% 0,100% 100%,0 100%);}
  .label--blend{left:538px;top:361px;width:182px;height:239px;clip-path:polygon(0 40px,100% 0,100% 100%,0 100%);}
  .label--atf{left:921px;top:431px;width:124px;height:175px;clip-path:polygon(0 26px,100% 0,100% 100%,0 100%);}

  .line{position:absolute;white-space:nowrap;line-height:1;text-align:right;}
  .line--title{font-weight:800;letter-spacing:.02em;}
  .line--range{font-weight:300;letter-spacing:.03em;}
  .line--grade{font-weight:800;letter-spacing:.01em;}
  .line--claim{font-weight:400;}
  .bullet::after{content:"";display:inline-block;width:6px;height:6px;border-radius:50%;background:var(--dot);margin-left:6px;vertical-align:middle;}

  .grade-band{
    position:absolute;right:1px;background:var(--band);
    display:flex;align-items:center;justify-content:center;
    font-weight:700;letter-spacing:.03em;
  }
</style>
</head>
<body>

<!-- Drawing sheet with size callouts -->
<svg class="sheet" viewBox="0 0 1200 927" aria-hidden="true">
  <defs>
    <marker id="arrow" viewBox="0 0 10 10" refX="10" refY="5" markerWidth="6" markerHeight="6" orient="auto-start-reverse">
      <path d="M0 2 L10 5 L0 8Z" fill="var(--dim-line)"/>
    </marker>
  </defs>
  <rect x="21.5" y="161.5" width="1147" height="598" fill="none" stroke="var(--sheet-line)"/>
  <g stroke="var(--ext-line)" stroke-width=".6">
    <line x1="78" y1="368" x2="135" y2="368"/><line x1="78" y1="598" x2="135" y2="598"/>
    <line x1="325" y1="325" x2="436" y2="325"/><line x1="325" y1="598" x2="436" y2="598"/>
    <line x1="136" y1="598" x2="136" y2="667"/><line x1="325" y1="598" x2="325" y2="667"/>
    <line x1="482" y1="404" x2="538" y2="404"/><line x1="482" y1="600" x2="538" y2="600"/>
    <line x1="720" y1="362" x2="832" y2="362"/><line x1="720" y1="600" x2="832" y2="600"/>
    <line x1="538" y1="600" x2="538" y2="668"/><line x1="720" y1="600" x2="720" y2="668"/>
    <line x1="875" y1="461" x2="921" y2="461"/><line x1="875" y1="605" x2="921" y2="605"/>
    <line x1="1045" y1="431" x2="1099" y2="431"/><line x1="1045" y1="605" x2="1099" y2="605"/>
    <line x1="921" y1="606" x2="921" y2="669"/><line x1="1044" y1="606" x2="1044" y2="669"/>
  </g>
  <g stroke="var(--dim-line)" stroke-width=".7" marker-start="url(#arrow)" marker-end="url(#arrow)">
    <line x1="82" y1="370" x2="82" y2="596"/>
    <line x1="432" y1="327" x2="432" y2="596"/>
    <line x1="138" y1="663" x2="323" y2="663"/>
    <line x1="486" y1="406" x2="486" y2="598"/>
    <line x1="828" y1="364" x2="828" y2="598"/>
    <line x1="540" y1="664" x2="718" y2="664"/>
    <line x1="879" y1="463" x2="879" y2="603"/>
    <line x1="1095" y1="433" x2="1095" y2="603"/>
    <line x1="923" y1="665" x2="1042" y2="665"/>
  </g>
</svg>
<div class="dim-value" style="left:82px;top:483px;">171.67</div>
<div class="dim-value" style="left:432px;top:447px;">204.18</div>
<div class="dim-value" style="left:220px;top:663px;">141.43</div>
<div class="dim-value" style="left:486px;top:473px;">146.21</div>
<div class="dim-value" style="left:828px;top:481px;">177.35</div>
<div class="dim-value" style="left:625px;top:664px;">135.45</div>
<div class="dim-value" style="left:879px;top:526px;">108.20</div>
<div class="dim-value" style="left:1095px;top:515px;">129.63</div>
<div class="dim-value" style="left:982px;top:665px;">92.58</div>

<!-- Full synthetic -->
<section class="label label--full">
  <svg viewBox="0 0 190 273" preserveAspectRatio="none" aria-hidden="true">
    <defs>
      <radialGradient id="sky-full" cx="0.55" cy="0.5" r="0.7">
        <stop offset="0" stop-color="var(--sky-light)"/>
        <stop offset="0.55" stop-color="var(--sky-mid)"/>
        <stop offset="1" stop-color="var(--sky-deep)"/>
      </radialGradient>
    </defs>
    <rect width="190" height="273" fill="url(#sky-full)"/>
    <path d="M16 0 Q20 150 92 273 L106 273 Q38 150 50 0Z" fill="var(--stripe)" opacity=".7"/>
  </svg>
  <svg viewBox="0 0 190 273" preserveAspectRatio="none" role="img" aria-label="Blue digital network and gear illustration">
    <defs>
      <linearGradient id="net-full" x1="0" y1="0" x2="0" y2="1">
        <stop offset="0" stop-color="var(--navy)"/>
        <stop offset="1" stop-color="var(--navy-mid)"/>
      </linearGradient>
    </defs>
    <path d="M0 0 L26 0 Q30 150 105 273 L0 273Z" fill="url(#net-full)"/>
  </svg>
  <svg viewBox="0 0 190 273" preserveAspectRatio="none" role="img" aria-label="Golden motor oil splash">
    <defs>
      <radialGradient id="oil-full" cx="0.6" cy="0.6" r="0.55">
        <stop offset="0" stop-color="var(--gold-light)" stop-opacity=".95"/>
        <stop offset="0.6" stop-color="var(--gold)" stop-opacity=".6"/>
        <stop offset="1" stop-color="var(--gold)" stop-opacity="0"/>
      </radialGradient>
    </defs>
    <rect x="75" y="185" width="120" height="70" fill="url(#oil-full)"/>
  </svg>
  <div class="line line--title" style="right:7px;top:42px;font-size:15.5px;">BRIXTANE HIGH</div>
  <div class="line line--title" style="right:7px;top:61px;font-size:15.5px;">PERFORMANCE</div>
  <div class="line line--range" style="right:9px;top:84px;font-size:12px;">FULL SYNTHETIC</div>
  <div class="line line--grade" style="right:9px;top:104px;font-size:16px;">0W-20/5W-30</div>
  <div class="line line--claim bullet" style="right:11px;top:138px;font-size:9px;">Maximum Protection</div>
  <div class="line line--claim bullet" style="right:11px;top:151px;font-size:9px;">Ultimate Performance</div>
  <div class="line line--claim bullet" style="right:11px;top:167px;font-size:9px;">Brixtane Quendor</div>
  <div class="grade-band" style="left:91px;top:242px;height:22px;font-size:11px;">0W-16/5W-20</div>
</section>

<!-- Synthetic blend -->
<section class="label label--blend">
  <svg viewBox="0 0 182 239" preserveAspectRatio="none" aria-hidden="true">
    <defs>
      <radialGradient id="sky-blend" cx="0.55" cy="0.5" r="0.7">
        <stop offset="0" stop-color="var(--sky-light)"/>
        <stop offset="0.55" stop-color="var(--sky-mid)"/>
        <stop offset="1" stop-color="var(--sky-deep)"/>
      </radialGradient>
    </defs>
    <rect width="182" height="239" fill="url(#sky-blend)"/>
    <path d="M14 0 Q18 130 80 239 L94 239 Q34 130 46 0Z" fill="var(--stripe)" opacity=".7"/>
  </svg>
  <svg viewBox="0 0 182 239" preserveAspectRatio="none" role="img" aria-label="Blue digital network and gear illustration">
    <defs>
      <linearGradient id="net-blend" x1="0" y1="0" x2="0" y2="1">
        <stop offset="0" stop-color="var(--navy)"/>
        <stop offset="1" stop-color="var(--navy-mid)"/>
      </linearGradient>
    </defs>
    <path d="M0 0 L22 0 Q26 130 93 239 L0 239Z" fill="url(#net-blend)"/>
  </svg>
  <svg viewBox="0 0 182 239" preserveAspectRatio="none" role="img" aria-label="Golden motor oil splash">
    <defs>
      <radialGradient id="oil-blend" cx="0.6" cy="0.6" r="0.55">
        <stop offset="0" stop-color="var(--gold-light)" stop-opacity=".95"/>
        <stop offset="0.6" stop-color="var(--gold)" stop-opacity=".6"/>
        <stop offset="1" stop-color="var(--gold)" stop-opacity="0"/>
      </radialGradient>
    </defs>
    <rect x="65" y="160" width="122" height="60" fill="url(#oil-blend)"/>
  </svg>
  <div class="line line--title" style="right:7px;top:34px;font-size:15px;">BRIXTANE</div>
  <div class="line line--title" style="right:7px;top:53px;font-size:15px;">QUENDOR</div>
  <div class="line line--range" style="right:7px;top:76px;font-size:11px;">SYNTHETIC BLEND</div>
  <div class="line line--grade" style="right:7px;top:99px;font-size:15px;">10W-40/5W-30</div>
  <div class="line line--claim" style="right:7px;top:126px;font-size:8px;">The perfect combination</div>
  <div class="line line--claim" style="right:7px;top:138px;font-size:8px;">of durability and</div>
  <div class="line line--claim" style="right:7px;top:150px;font-size:8px;">efficiency</div>
  <div class="grade-band" style="left:89px;top:211px;height:21px;font-size:12px;">5W-20</div>
</section>

<!-- Transmission fluid -->
<section class="label label--atf">
  <svg viewBox="0 0 124 175" preserveAspectRatio="none" aria-hidden="true">
    <defs>
      <radialGradient id="sky-atf" cx="0.55" cy="0.5" r="0.7">
        <stop offset="0" stop-color="var(--sky-light)"/>
        <stop offset="0.55" stop-color="var(--sky-mid)"/>
        <stop offset="1" stop-color="var(--sky-deep)"/>
      </radialGradient>
    </defs>
    <rect width="124" height="175" fill="url(#sky-atf)"/>
    <path d="M10 0 Q12 95 55 175 L65 175 Q24 95 33 0Z" fill="var(--stripe)" opacity=".7"/>
  </svg>
  <svg viewBox="0 0 124 175" preserveAspectRatio="none" role="img" aria-label="Blue digital network and gear illustration">
    <defs>
      <linearGradient id="net-atf" x1="0" y1="0" x2="0" y2="1">
        <stop offset="0" stop-color="var(--navy)"/>
        <stop offset="1" stop-color="var(--navy-mid)"/>
      </linearGradient>
    </defs>
    <path d="M0 0 L15 0 Q18 95 68 175 L0 175Z" fill="url(#net-atf)"/>
  </svg>
  <svg viewBox="0 0 124 175" preserveAspectRatio="none" role="img" aria-label="Golden transmission fluid splash">
    <defs>
      <radialGradient id="oil-atf" cx="0.6" cy="0.6" r="0.55">
        <stop offset="0" stop-color="var(--gold-light)" stop-opacity=".95"/>
        <stop offset="0.6" stop-color="var(--gold)" stop-opacity=".6"/>
        <stop offset="1" stop-color="var(--gold)" stop-opacity="0"/>
      </radialGradient>
    </defs>
    <rect x="50" y="115" width="80" height="45" fill="url(#oil-atf)"/>
  </svg>
  <div class="line line--title" style="right:7px;top:18px;font-size:10.5px;">BRIXTANE</div>
  <div class="line line--title" style="right:7px;top:33px;font-size:10.5px;">GELVORIA</div>
  <div class="line line--title" style="right:7px;top:48px;font-size:10.5px;">TRANSMISSION</div>
  <div class="line line--title" style="right:7px;top:63px;font-size:10.5px;">FLUID ATF</div>
  <div class="line line--title" style="right:7px;top:78px;font-size:10.5px;">III</div>
  <div class="line line--claim" style="right:7px;top:94px;font-size:7.5px;">proven to Maximize</div>
  <div class="line line--claim" style="right:7px;top:106px;font-size:7.5px;">Transmission Life</div>
  <div class="grade-band" style="left:60px;top:155px;height:14px;font-size:9px;">5W-20</div>
</section>

</body>
</html>
```